Relocation Company Flyer Design

We require a redesign of our existing flyer (attached). We are a relocation company, based in Muscat, Oman, which provides individual, corporate and industrial relocation services.
The design needs to follow the color as per the existing flyer and should retain the text.

Industry/Entity Type

It Company

```html
<!DOCTYPE html>
<html lang="en">
<head>
<meta charset="utf-8">
<title>Wayfare Relocation Flyer</title>
<link rel="stylesheet" href="https://fonts.googleapis.com/css2?family=Oswald:wght@500;600&family=Signika:wght@400;500&family=Lato:wght@400;700&display=swap">
<style>
  :root {
    --navy: #0d1f4a;
    --royal: #1a5fc4;
    --sky: #19a8ec;
    --brand-blue: #1662c4;
    --white: #ffffff;
    --shadow-grey: #9aa3ad;
    --page: #e9ecef;
    --icon-grey: #d9dde2;
  }
  * { margin: 0; padding: 0; box-sizing: border-box; }
  html, body { width: 1200px; height: 1000px; overflow: hidden; background: var(--page); }
  .flyer {
    position: absolute; left: 234px; top: 30px;
    width: 618px; height: 794px;
    transform: scale(1.1839); transform-origin: top left;
    background: var(--navy);
    overflow: hidden;
    font-family: "Lato", sans-serif; color: var(--white);
  }
  .flyer-shapes { position: absolute; inset: 0; }
  .headline { position: absolute; left: 10px; top: 20px; }
  .headline-moving { font-family: "Oswald", sans-serif; font-weight: 500; font-size: 52px; line-height: 68px; letter-spacing: 1px; }
  .headline-let, .headline-handle { font-family: "Signika", sans-serif; font-size: 28px; line-height: 40px; }
  .headline-pro { font-family: "Oswald", sans-serif; font-weight: 500; font-size: 38px; line-height: 44px; letter-spacing: 1px; }
  .brand { position: absolute; left: 26px; top: 278px; width: 300px; }
  .brand-name { font-family: "Lato", sans-serif; font-weight: 700; font-size: 58px; line-height: 62px; color: var(--brand-blue); }
  .brand-tagline { font-family: "Lato", sans-serif; font-weight: 700; font-size: 15px; line-height: 20px; color: var(--brand-blue); }
  .section-tab {
    position: absolute; left: 0; height: 32px;
    background: var(--white); color: var(--navy);
    font-family: "Oswald", sans-serif; font-weight: 600; font-size: 22px; line-height: 32px;
    padding-left: 12px;
    clip-path: polygon(0 0, calc(100% - 16px) 0, 100% 50%, calc(100% - 16px) 100%, 0 100%);
  }
  .tab-services { top: 420px; width: 170px; }
  .tab-contact { top: 595px; width: 170px; }
  .tab-follow { top: 696px; width: 160px; }
  .services { position: absolute; left: 24px; top: 458px; list-style: none; }
  .services li { font-size: 14px; line-height: 22px; letter-spacing: .3px; position: relative; }
  .services li::before { content: ""; position: absolute; left: -13px; top: 9px; width: 5px; height: 5px; border-radius: 50%; background: var(--white); }
  .office { position: absolute; top: 634px; }
  .office-oman { left: 12px; }
  .office-qatar { left: 168px; }
  .office-name { font-family: "Oswald", sans-serif; font-weight: 500; font-size: 18px; line-height: 24px; }
  .office-row { font-size: 9px; line-height: 13px; display: flex; }
  .office-row span:first-child { width: 40px; }
  .social { position: absolute; top: 738px; left: 10px; display: flex; align-items: center; gap: 8px; font-size: 11px; }
  .social-icon { width: 18px; height: 18px; background: var(--sky); border-radius: 3px; }
  .social-icon.round { border-radius: 50%; background: var(--icon-grey); margin-left: 18px; }
</style>
</head>
<body>
<main class="flyer">
  <svg class="flyer-shapes" viewBox="0 0 618 794" width="618" height="794">
    <defs>
      <linearGradient id="glow" x1="0" y1="0" x2="1" y2="0">
        <stop offset="0" stop-color="#0d1f4a"/>
        <stop offset="1" stop-color="#1a5fc4"/>
      </linearGradient>
      <linearGradient id="photo" x1="0" y1="0" x2="0" y2="1">
        <stop offset="0" stop-color="#d9c9a3"/>
        <stop offset=".45" stop-color="#3f79c9"/>
        <stop offset=".8" stop-color="#c29a63"/>
        <stop offset="1" stop-color="#8aa7c9"/>
      </linearGradient>
    </defs>
    <rect class="base" width="618" height="794" fill="#0d1f4a"/>
    <path class="glow-band" d="M300,0 L470,0 L322,405 L400,770 L330,770 L250,405 Z" fill="url(#glow)" opacity=".85"/>
    <path class="inner-line" d="M398,0 L408,0 L292,330 L388,766 L378,766 L282,330 Z" fill="#ffffff"/>
    <path class="sky-band" d="M470,0 L505,0 L357,405 L435,770 L400,770 L322,405 Z" fill="#19a8ec"/>
    <path class="white-band" d="M510,0 L540,0 L392,405 L470,770 L440,770 L362,405 Z" fill="#ffffff"/>
    <path class="photo-area" role="img" aria-label="Photo of a mover in a blue cap and shirt carrying cardboard boxes" d="M545,0 L618,0 L618,770 L470,770 L395,405 Z" fill="url(#photo)"/>
    <rect class="bottom-line" x="0" y="764" width="618" height="6" fill="#ffffff"/>
    <rect class="bottom-band" x="0" y="772" width="618" height="22" fill="#19a8ec"/>
    <path class="banner-shadow" d="M0,252 L340,252 L392,325 L340,398 L0,398 Z" fill="#9aa3ad" opacity=".7"/>
    <path class="brand-banner" d="M0,241 L334,241 L385,314 L334,388 L0,388 Z" fill="#ffffff"/>
    <rect class="boxes-area" role="img" aria-label="Stack of yellow moving boxes" x="405" y="628" width="185" height="154" rx="2" fill="#f3d23a"/>
  </svg>

  <header class="headline">
    <div class="headline-moving">MOVING ?</div>
    <div class="headline-let">Let the</div>
    <div class="headline-pro">PROFESSIONAL S</div>
    <div class="headline-handle">Handle your move</div>
  </header>

  <div class="brand">
    <div class="brand-name">Wayfare</div>
    <div class="brand-tagline">relocation across the gulf</div>
  </div>

  <div class="section-tab tab-services">OUR SERVICES</div>
  <ul class="services">
    <li>International Relocations</li>
    <li>Local Storage &amp; Relocations</li>
    <li>Vehicle Storage &amp; Relocations</li>
    <li>Pet Relocations</li>
    <li>Corporate &amp; Industrial Relocations</li>
    <li>Short-term &amp; Long-term Warehousing</li>
  </ul>

  <div class="section-tab tab-contact">CONTACT US</div>
  <div class="office office-oman">
    <div class="office-name">OMAN</div>
    <div class="office-row"><span>Phone</span><span>: +968 9100 24 68</span></div>
    <div class="office-row"><span>Email</span><span>: relo@wayfareoman.com</span></div>
  </div>
  <div class="office office-qatar">
    <div class="office-name">QATAR</div>
    <div class="office-row"><span>Phone</span><span>: 974 4000 1357/8</span></div>
    <div class="office-row"><span>Email</span><span>: sales@wayfareqatar.com</span></div>
  </div>

  <div class="section-tab tab-follow">FOLLOW US</div>
  <div class="social">
    <span class="social-icon"></span><span>/wayfareoman</span>
    <span class="social-icon round"></span><span>www.wayfareoman.com</span>
  </div>
</main>
</body>
</html>
```